Creative & Appealing Business Card

Required a business card for Vantrelink
We specialise in claims management services for PPI ( Payment Protection Insurance.
2 sided business card
Round Corners
I like embossed and raised lettering

```html
<!DOCTYPE html>
<html lang="en">
<head>
<meta charset="utf-8">
<title>Vantrelink – Business Card</title>
<link rel="stylesheet" href="https://fonts.googleapis.com/css2?family=Rokkitt:wght@400&family=Montserrat:wght@500;600&family=Ubuntu:wght@300;700&display=swap">
<style>
  :root {
    --ink-slate: #354a53;
    --brand-red: #b71d23;
    --paper: #fdfdfd;
    --page: #ffffff;
    --card-edge: #c9c9c9;
    --card-shadow: #bdbdbd;
    --back-text: #e2e6e8;
    --radius: 29px;
  }
  * { box-sizing: border-box; margin: 0; padding: 0; }
  html, body {
    width: 892px;
    height: 1200px;
    overflow: hidden;
    background: var(--page);
  }
  .sheet { position: relative; width: 892px; height: 1200px; }

  .card {
    position: absolute;
    left: 21px;
    width: 851px;
    height: 567px;
    border-radius: var(--radius);
    overflow: hidden;
  }

  /* Front */
  .card--front {
    top: 25px;
    background: var(--paper);
    border: 1px solid var(--card-edge);
  }
  .card__artwork {
    position: absolute;
    inset: 0;
    background: linear-gradient(160deg, var(--ink-slate) 0%, var(--ink-slate) 30%, var(--brand-red) 60%, var(--brand-red) 100%);
    clip-path: polygon(0 0, 250px 0, 250px 330px, 100% 330px, 100% 100%, 0 100%);
  }
  .brand {
    position: absolute;
    left: 318px;
    top: 152px;
    display: flex;
    align-items: center;
    gap: 24px;
  }
  .brand__dot {
    width: 68px;
    height: 68px;
    border-radius: 50%;
    background: var(--ink-slate);
  }
  .brand__name {
    font-family: "Rokkitt", Georgia, serif;
    font-size: 84px;
    line-height: 1;
    color: var(--ink-slate);
  }
  .services {
    position: absolute;
    left: 413px;
    top: 242px;
    font-family: "Montserrat", Arial, sans-serif;
    font-size: 16px;
    line-height: 22px;
    color: var(--ink-slate);
    font-weight: 500;
    list-style: none;
  }
  .services__title { color: var(--brand-red); font-weight: 600; margin-left: 2px; }

  /* Back */
  .card--back {
    top: 614px;
    background: var(--ink-slate);
    box-shadow: 8px 8px 0 var(--card-shadow);
  }
  .holder {
    position: absolute;
    right: 521px;
    top: 306px;
    font-family: "Ubuntu", Arial, sans-serif;
    font-weight: 700;
    font-size: 30px;
    color: var(--back-text);
  }
  .contact {
    position: absolute;
    top: 370px;
    left: 0;
    width: 100%;
    font-family: "Ubuntu", Arial, sans-serif;
    font-weight: 300;
    font-size: 25px;
    line-height: 33.5px;
    color: var(--back-text);
  }
  .contact__address {
    position: absolute;
    right: 521px;
    text-align: right;
    font-style: normal;
  }
  .contact__divider {
    position: absolute;
    left: 346px;
    top: 0;
    width: 3px;
    height: 120px;
    background: var(--back-text);
  }
  .contact__lines {
    position: absolute;
    left: 364px;
    list-style: none;
  }
</style>
</head>
<body>
<main class="sheet">

  <section class="card card--front" aria-label="Card front">
    <div class="card__artwork" role="img" aria-label="Flowing red and dark slate flame swoosh artwork sweeping down the left side and across the bottom of the card"></div>

    <div class="brand">
      <span class="brand__dot" aria-hidden="true"></span>
      <span class="brand__name">Vantrelink</span>
    </div>

    <ul class="services">
      <li class="services__title">Claims Management Service for Mis-sold</li>
      <li>- Payment Protection Insurance Claims</li>
      <li>- Interest Rate Hedging Products / SWAPS</li>
    </ul>
  </section>

  <section class="card card--back" aria-label="Card back">
    <p class="holder">Tariq Mendel</p>
    <div class="contact">
      <address class="contact__address">48<br>Alder Grove Road<br>London<br>N4 2QP</address>
      <span class="contact__divider" aria-hidden="true"></span>
      <ul class="contact__lines">
        <li>e: tariq@vantrelink.com</li>
        <li>t: +44 (0) 333 014 0871</li>
        <li>f: +44 (0) 203 912 4466</li>
        <li>w: www.vantrelink.com</li>
      </ul>
    </div>
  </section>

</main>
</body>
</html>
```